Wild Ridge Trekcraft DL flyer

I'm looking for a new flyer for my startup business. In Darwin Australia.
Aimed at family's and short stay tourists the "Wild Ridge Trekcraft" 4 hr tour will give people a basic understanding of some essential bush survival skills in the Australian Outback.
things covered in this 4 hr tour are
1. Finding water.
2. finding food.
3. Finding/making shelter and fire.
4. Finding your way home.

The tour will pick clients up in an air conditioned purpose build 4WD and take them to a nearby bushland area where they will have the opportunity to catch and harvest some native bushtucker.
They will then be able to find/harvest some water for survival situations.
While we cook our bush tucker they will also learn to find their way home through ancient navigation techniques as well.

Clients will then be dropped back to their accomodation with some fun and vital knowledge of surviving in the Australian outback.
At the end of the tour the group will be able to take home a basic survival kit which they will be able to use through the skills they just gained on the tour.

I'd like a two sided DL size flyer emphasising the following points.
4hr/half day tour
Fun for the family
Free survival kit included.
Eat what you catch
Learn essential survival skills
Provided buy an experienced and passionate bushman.
$150/head including transfers.

I'll provide some pictures for the flyer and any extra content you require.
Updates

Target Market(s)

Family's
Short stay tourists

Industry/Entity Type

Tourism

Colors

Designer to choose colors to be used in the design.

Requirements
Must have
• As per brief
Nice to have
• Any extra content and flair designers would like to add
Should not have
• Any images which aren't Australian

```html
<!DOCTYPE html>
<html lang="en">
<head>
<meta charset="utf-8">
<title>Wild Ridge Trekcraft – DL Flyer</title>
<link href="https://fonts.googleapis.com/css2?family=Rubik+Dirt&family=Lato:wght@400;700;900&display=swap" rel="stylesheet">
<style>
  :root{
    --canvas:#d9d9d6;
    --earth-dark:#5a3e22;
    --earth-mid:#8b6a43;
    --earth-light:#a8875c;
    --rust:#b4602e;
    --paper:#f1f0ed;
    --ink:#2a2a2a;
    --white:#ffffff;
    --bush-dark:#3f5d2a;
    --bush-light:#8fa85a;
  }
  *{box-sizing:border-box;margin:0;padding:0}
  html,body{width:1200px;height:974px;overflow:hidden}
  body{background:var(--canvas);font-family:'Lato',sans-serif;color:var(--ink);position:relative}

  .flyer{position:absolute;top:57px;width:410px;height:860px;background:var(--paper);overflow:hidden;box-shadow:0 6px 18px rgba(0,0,0,.25)}
  .flyer--front{left:150px}
  .flyer--back{left:640px}

  .header{position:absolute;left:0;top:0;width:100%;height:160px;
    background:radial-gradient(ellipse at 40% 40%,var(--earth-light),var(--earth-mid) 45%,var(--earth-dark));}
  .title{position:absolute;top:28px;left:0;width:100%;text-align:center;font-family:'Rubik Dirt',sans-serif;
    color:var(--white);font-size:46px;line-height:46px;letter-spacing:1px;z-index:3}

  .photo{position:absolute;left:0;top:130px;width:100%}
  .photo--outback{height:380px;background:linear-gradient(180deg,#8fb6d0 0%,#6f9a52 22%,var(--bush-dark) 45%,#7b8d3e 65%,#a8562c 85%,var(--bush-light) 100%)}
  .photo--guide{height:350px;background:linear-gradient(160deg,#5a7a3a 0%,#9c7a5c 40%,#c7906c 55%,#4c6a36 80%,#6f8a4a 100%)}

  .tear{position:absolute;left:0;width:100%;display:block;z-index:2}
  .tear--head{top:140px;height:40px}
  .tear--paper{height:50px}
  .tear--foot{height:34px}

  .paper{position:absolute;left:0;width:100%;background:var(--paper)}
  .footer{position:absolute;left:0;bottom:0;width:100%;background:var(--rust);color:var(--white)}

  .badge{position:absolute;width:176px;height:176px;border-radius:50%;background:var(--rust);
    border:5px solid var(--white);color:var(--white);text-align:center;z-index:4;
    display:flex;flex-direction:column;justify-content:center;align-items:center}
  .badge__big{font-family:'Rubik Dirt',sans-serif;font-size:40px;line-height:42px}
  .badge__big--price{font-size:22px;line-height:28px;white-space:nowrap}
  .badge__small{font-size:20px;line-height:22px;font-weight:400}

  /* front */
  .flyer--front .tear--paper{top:470px}
  .flyer--front .paper{top:510px;height:350px}
  .flyer--front .badge{left:232px;top:405px}
  .topics{position:absolute;left:24px;top:592px;z-index:3}
  .topics__head{display:flex;align-items:center;gap:10px;margin-bottom:14px}
  .topics__title{font-family:'Rubik Dirt',sans-serif;font-size:18px;line-height:20px;color:var(--ink)}
  .topics__title .accent{color:var(--rust)}
  .topics__list{list-style:none}
  .topics__item{display:flex;align-items:center;gap:8px;font-size:14px;line-height:17px;margin-bottom:10px}
  .dot-icon{width:16px;height:16px;border-radius:50%;background:var(--rust);flex:none;position:relative}
  .dot-icon::after{content:"";position:absolute;left:5px;top:5px;width:6px;height:6px;border-radius:50%;background:var(--white)}
  .portrait{position:absolute;right:0;bottom:60px;width:140px;height:150px;z-index:3;
    background:linear-gradient(180deg,#d8d3cc 0%,#a88a6a 45%,#e8e6e2 75%,#cfcac2 100%)}
  .flyer--front .footer{height:66px}
  .flyer--front .tear--foot{bottom:60px}

  /* back */
  .flyer--back .tear--paper{top:440px}
  .flyer--back .paper{top:480px;height:380px}
  .flyer--back .badge{left:218px;top:390px}
  .tour{position:absolute;left:20px;top:500px;width:370px;z-index:3}
  .tour__head{font-size:16px;font-weight:700;letter-spacing:.5px;line-height:22px;margin-bottom:2px}
  .tour__points{list-style:none;font-size:13px;font-weight:700;line-height:16px}
  .tour__points li{display:flex;align-items:center;gap:8px;margin-bottom:4px}
  .tour__points li::before{content:"";width:10px;height:10px;border-radius:50%;background:var(--rust);flex:none}
  .tour__copy{font-size:12px;line-height:15px;margin-top:8px}
  .flyer--back .footer{height:110px}
  .flyer--back .tear--foot{bottom:104px}
  .contact__title{text-align:center;font-size:16px;font-weight:700;text-decoration:underline;margin-top:14px;letter-spacing:.5px}
  .contact__row{display:flex;justify-content:space-between;align-items:center;padding:0 18px;margin-top:22px;font-size:12px}
  .contact__item{display:flex;align-items:center;gap:5px}
</style>
</head>
<body>

<section class="flyer flyer--front">
  <div class="header"></div>
  <h1 class="title">WILD RIDGE<br>TREKCRAFT</h1>
  <div class="photo photo--outback" role="img" aria-label="Photo of outback bushland with tall red termite mounds among gum trees and grass"></div>
  <svg class="tear tear--head" viewBox="0 0 410 40" preserveAspectRatio="none"><path fill="#6e5132" d="M0 0H410V20L395 28 380 18 362 32 345 22 330 30 312 16 298 26 280 14 262 24 246 12 230 22 214 14 198 26 180 16 164 28 146 18 128 30 110 20 92 34 76 24 58 34 42 22 24 30 10 20 0 26Z"/></svg>
  <svg class="tear tear--paper" viewBox="0 0 410 50" preserveAspectRatio="none"><path fill="#f1f0ed" d="M0 30L14 24 28 34 44 26 60 36 78 28 96 38 112 30 130 40 148 32 166 42 184 34 202 44 220 36 238 46 256 38 274 42 292 34 310 44 328 36 346 40 364 30 382 38 398 30 410 36V50H0Z"/></svg>
  <div class="paper"></div>
  <div class="badge"><span class="badge__big">FREE</span><span class="badge__small">Survival kit<br>included</span></div>
  <div class="topics">
    <div class="topics__head">
      <svg width="30" height="34" viewBox="0 0 30 34" aria-hidden="true"><path fill="#b4602e" d="M2 0H28V4H25C25 12 18 14 18 17 18 20 25 22 25 30H28V34H2V30H5C5 22 12 20 12 17 12 14 5 12 5 4H2Z"/></svg>
      <p class="topics__title">THINGS COVERED IN THIS<br><span class="accent">4 HR</span> TOUR ARE :</p>
    </div>
    <ul class="topics__list">
      <li class="topics__item"><span class="dot-icon"></span>Finding water.</li>
      <li class="topics__item"><span class="dot-icon"></span>Finding food.</li>
      <li class="topics__item"><span class="dot-icon"></span>Finding/making shelter and fire.</li>
      <li class="topics__item"><span class="dot-icon"></span>Finding your way home.</li>
    </ul>
  </div>
  <div class="portrait" role="img" aria-label="Photo of the bushman guide in a wide-brim hat and sunglasses"></div>
  <svg class="tear tear--foot" viewBox="0 0 410 34" preserveAspectRatio="none"><path fill="#b4602e" d="M0 14L16 8 32 16 50 6 68 14 86 4 104 12 122 6 140 16 158 8 176 14 194 4 212 12 230 6 248 14 266 8 284 16 302 6 320 12 338 4 356 14 374 8 392 14 410 6V34H0Z"/></svg>
  <div class="footer"></div>
</section>

<section class="flyer flyer--back">
  <div class="header"></div>
  <h1 class="title">WILD RIDGE<br>TREKCRAFT</h1>
  <div class="photo photo--guide" role="img" aria-label="Photo of the guide by a mangrove creek holding up a freshly caught mud crab"></div>
  <svg class="tear tear--head" viewBox="0 0 410 40" preserveAspectRatio="none"><path fill="#6e5132" d="M0 0H410V24L392 16 376 30 358 20 340 28 324 14 306 26 288 18 270 30 252 20 236 28 218 16 200 26 184 18 166 32 148 22 130 30 112 18 94 28 78 20 60 32 42 22 26 30 12 18 0 24Z"/></svg>
  <svg class="tear tear--paper" viewBox="0 0 410 50" preserveAspectRatio="none"><path fill="#f1f0ed" d="M0 20L16 28 32 18 50 30 66 22 84 32 100 24 118 36 136 28 154 38 172 30 190 40 208 34 226 42 244 36 262 44 280 38 298 46 316 40 334 44 352 38 370 46 388 40 410 44V50H0Z"/></svg>
  <div class="paper"></div>
  <div class="badge"><span class="badge__big badge__big--price">$150/HEAD</span><span class="badge__small">including<br>transfers</span></div>
  <div class="tour">
    <p class="tour__head">THE TOUR IS :</p>
    <ul class="tour__points">
      <li>Fun for the family</li>
      <li>Learn essential survival skills</li>
      <li>Provided buy an experienced and passionate bushman.</li>
    </ul>
    <p class="tour__copy">The tour will pick you up in an air conditioned purpose build 4WD and take them to a nearby bushland area where they will have the opportunity to catch and harvest some native bushtucker. They will then be able to find/harvest some water for survival situations. While we cook our bush tucker they will also learn to find their way home through ancient navigation techniques as well.</p>
  </div>
  <svg class="tear tear--foot" viewBox="0 0 410 34" preserveAspectRatio="none"><path fill="#b4602e" d="M0 10L18 16 36 6 54 14 72 4 90 12 108 8 126 16 144 6 162 14 180 4 198 12 216 8 234 16 252 6 270 14 288 4 306 12 324 8 342 16 360 6 378 12 396 4 410 10V34H0Z"/></svg>
  <div class="footer">
    <p class="contact__title">CONTACT US:</p>
    <div class="contact__row">
      <span class="contact__item"><svg width="13" height="13" viewBox="0 0 24 24" aria-hidden="true"><path fill="#fff" d="M6.6 10.8a15 15 0 0 0 6.6 6.6l2.2-2.2c.3-.3.7-.4 1-.2 1.1.4 2.3.6 3.6.6.6 0 1 .4 1 1V20c0 .6-.4 1-1 1A17 17 0 0 1 3 4c0-.6.4-1 1-1h3.5c.6 0 1 .4 1 1 0 1.3.2 2.5.6 3.6.1.3 0 .7-.2 1z"/></svg>08 7000 4411</span>
      <span class="contact__item"><svg width="14" height="11" viewBox="0 0 24 18" aria-hidden="true"><rect x="1" y="1" width="22" height="16" rx="2" fill="none" stroke="#fff" stroke-width="2"/><path d="M1 2l11 8 11-8" fill="none" stroke="#fff" stroke-width="2"/></svg>hello@wildridgetrek.au</span>
      <span class="contact__item"><svg width="13" height="13" viewBox="0 0 24 24" aria-hidden="true"><circle cx="12" cy="12" r="10" fill="none" stroke="#fff" stroke-width="2"/><path d="M2 12h20M12 2c3 3 3 17 0 20M12 2c-3 3-3 17 0 20" fill="none" stroke="#fff" stroke-width="1.5"/></svg>www.wildridgetrek.au</span>
    </div>
  </div>
</section>

</body>
</html>
```